Business Card - Apex Wellness

Please use the logo / design elements and font to design a business card that is eye catching and informative. If using "Direct Primary Care" logo element, you don't have to spell it out in the text.

Dr. Brendan Halvik
Apex Wellness - Direct Primary Care
4817 Tillbrook Rd. Suite 305
Larkmont, AR 72000
Phone: 479-555-0137
ApexWellnessAR.example

```html
<!DOCTYPE html>
<html lang="en">
<head>
<meta charset="utf-8">
<title>Apex Wellness – Business Card</title>
<link href="https://fonts.googleapis.com/css2?family=Poppins:wght@400;500;600;700&display=swap" rel="stylesheet">
<style>
  :root {
    --stage: #222222;
    --navy: #071331;
    --sky: #49b9ea;
    --white: #ffffff;
    --card-w: 580px;
    --card-h: 331px;
  }
  * { margin: 0; padding: 0; box-sizing: border-box; }
  html, body { width: 1200px; height: 800px; overflow: hidden; }
  body {
    background: var(--stage);
    font-family: "Poppins", sans-serif;
    position: relative;
  }
  .card {
    position: absolute;
    width: var(--card-w);
    height: var(--card-h);
    background: var(--navy);
    border-radius: 24px;
    box-shadow: 0 6px 0 var(--sky), 0 16px 30px rgba(0,0,0,0.55);
    overflow: hidden;
  }
  .card--back { left: 60px; top: 50px; }
  .card--front { left: 560px; top: 412px; }

  .brand {
    display: flex;
    align-items: center;
    gap: 12px;
    color: var(--white);
    font-weight: 600;
    white-space: nowrap;
  }
  .brand__dot {
    border-radius: 50%;
    background: var(--sky);
    flex: none;
  }
  .card--back .brand {
    position: absolute;
    left: 50%; top: 50%;
    transform: translate(-50%, -50%);
    font-size: 46px;
    letter-spacing: 0.5px;
  }
  .card--back .brand__dot { width: 30px; height: 30px; }

  .front__panel {
    position: absolute;
    right: 0; top: 0;
    width: 170px; height: 100%;
    background: var(--sky);
  }
  .front__logo {
    position: absolute;
    left: 28px; top: 30px;
    font-size: 26px;
  }
  .front__logo .brand__dot { width: 18px; height: 18px; }

  .front__accent {
    position: absolute;
    left: 0; top: 152px;
    width: 12px; height: 58px;
    background: var(--sky);
  }
  .front__details {
    position: absolute;
    left: 32px; top: 150px;
    color: var(--white);
  }
  .person__name {
    color: var(--sky);
    font-weight: 700;
    font-size: 28px;
    line-height: 1.1;
  }
  .person__role {
    font-size: 14px;
    margin-top: 4px;
  }
  .address {
    font-size: 13px;
    line-height: 1.45;
    margin-top: 18px;
    font-style: normal;
  }
  .contact { list-style: none; margin-top: 12px; font-size: 13px; }
  .contact li { display: flex; align-items: center; gap: 8px; line-height: 1.6; }
  .contact svg { width: 14px; height: 14px; flex: none; }
</style>
</head>
<body>

  <section class="card card--back" aria-label="Card back">
    <div class="brand">
      <span class="brand__dot"></span>
      <span class="brand__name">Apex Wellness</span>
    </div>
  </section>

  <section class="card card--front" aria-label="Card front">
    <div class="front__panel"></div>

    <div class="brand front__logo">
      <span class="brand__dot"></span>
      <span class="brand__name">Apex Wellness</span>
    </div>

    <div class="front__accent"></div>

    <div class="front__details">
      <h1 class="person__name">Dr. Brendan Halvik</h1>
      <p class="person__role">Apex Wellness - Direct Primary Care</p>

      <address class="address">
        4817 Tillbrook Rd. Suite 305<br>
        Larkmont, AR 72000
      </address>

      <ul class="contact">
        <li>
          <svg viewBox="0 0 24 24" aria-hidden="true"><path fill="#49b9ea" d="M6.6 10.8a15.1 15.1 0 0 0 6.6 6.6l2.2-2.2a1 1 0 0 1 1-.25 11.4 11.4 0 0 0 3.6.57 1 1 0 0 1 1 1V20a1 1 0 0 1-1 1A17 17 0 0 1 3 4a1 1 0 0 1 1-1h3.5a1 1 0 0 1 1 1c0 1.25.2 2.45.57 3.57a1 1 0 0 1-.25 1z"/></svg>
          479-555-0137
        </li>
        <li>
          <svg viewBox="0 0 24 24" aria-hidden="true"><circle cx="12" cy="12" r="9.5" fill="none" stroke="#49b9ea" stroke-width="2"/><path d="M2.5 12h19M12 2.5c3 3 3 16 0 19M12 2.5c-3 3-3 16 0 19" fill="none" stroke="#49b9ea" stroke-width="1.6"/></svg>
          www.ApexWellnessAR.example
        </li>
      </ul>
    </div>
  </section>

</body>
</html>
```